Business Card design for Property Developer

We need a business card design for a Melbourne based Property Developer called "Kestrelmoor Holdings Pty Ltd".

We subdivide land and onsell to builders etc.

We already have a company logo, which is attached. Also I have attached the layout requirements from the printer. We would like a 2-sided design with one side displaying our logo by itself and the other with the required info, such as name, address, tel no., email, abn etc. The card will need to be used by 4 members of staff so name and contact details should be interchangable.
Updates

If possible, can you please write "name' "job position" "phone" "email" "address" on the card but leave them so I can add the details at a later time. Thank you. Also I plan on printing with UV spot printing as a background on the card. Keep this is mind when designing.

Thanks again.

Hello designers, please do not include pics of houses, house plansĀ or construction machinery etc as we really do not like the way it looks. Thank you.

Target Market(s)

Real Estate Agents, Land Owners, Local Council Departments, Govt Bodies, other Developers etc.

Industry/Entity Type

Business

Requirements
Must have
• 2-sided design with one side displaying our logo by itself and the other with the required info, such as name, address, tel no., email, abn etc.

```html
<!DOCTYPE html>
<html lang="en">
<head>
<meta charset="utf-8">
<title>Kestrelmoor Holdings – Business Card Presentation</title>
<link href="https://fonts.googleapis.com/css2?family=Arimo:ital,wght@0,400;0,700;1,400&display=swap" rel="stylesheet">
<style>
  :root {
    --page: #ffffff;
    --bleed-light: #c9c9c9;
    --bleed-navy: #4b4a78;
    --bleed-dark: #3c3c3c;
    --paper: #f4f4f4;
    --navy: #1d1f52;
    --black: #000000;
    --brand: #24358f;
    --accent: #1f5fc4;
    --contact: #5a8ed8;
    --label: #000000;
    --white: #ffffff;
  }
  * { margin: 0; padding: 0; box-sizing: border-box; }
  html, body { width: 1200px; height: 1051px; overflow: hidden; background: var(--page); }
  body { position: relative; font-family: "Arimo", Arial, sans-serif; }

  .card { position: absolute; width: 573px; height: 367px; border: 9px solid; overflow: hidden; }
  .card--front { left: 17px; top: 17px; background: var(--paper); border-color: var(--bleed-light); }
  .card--front-uv { left: 610px; top: 17px; background: var(--white); border-color: var(--bleed-light); }
  .card--back { left: 17px; top: 401px; background: var(--navy); border-color: var(--bleed-navy); }
  .card--back-uv { left: 610px; top: 401px; background: var(--black); border-color: var(--bleed-dark); }

  .feature-disc { position: absolute; left: 292px; top: 16px; width: 312px; height: 312px; border-radius: 50%; }
  .card--front .feature-disc { background: var(--accent); }
  .card--front-uv .feature-disc { background: var(--black); }

  .brand-block { position: absolute; left: 38px; top: 22px; width: 220px; text-align: center; }
  .brand-mark { width: 108px; height: 108px; border-radius: 50%; background: var(--brand); margin: 0 auto 16px; }
  .brand-name { color: var(--brand); font-weight: 700; font-size: 22px; letter-spacing: 0.5px; line-height: 1.05; }

  .contact { position: absolute; left: 71px; top: 211px; color: var(--contact); }
  .contact .name { font-size: 26px; line-height: 30px; }
  .contact .line { font-size: 14.5px; line-height: 18px; }
  .contact .position { padding-left: 42px; }

  .back-logo { position: absolute; left: 0; right: 0; top: 108px; text-align: center; }
  .back-logo .brand-mark { width: 70px; height: 70px; background: var(--white); margin-bottom: 10px; }
  .back-logo .brand-name { color: var(--white); font-size: 15px; }

  .thumb { position: absolute; width: 127px; height: 82px; border: 2px solid; overflow: hidden; }
  .thumb--front { left: 17px; top: 781px; background: var(--paper); border-color: var(--bleed-light); }
  .thumb--back { left: 610px; top: 781px; background: var(--navy); border-color: var(--bleed-navy); }
  .thumb--front-uv { left: 17px; top: 876px; background: var(--white); border-color: var(--bleed-light); }
  .thumb--back-uv { left: 610px; top: 876px; background: var(--black); border-color: var(--bleed-dark); }
  .thumb .mini-disc { position: absolute; left: 65px; top: 4px; width: 70px; height: 70px; border-radius: 50%; }
  .thumb--front .mini-disc { background: var(--accent); }
  .thumb--front-uv .mini-disc { background: var(--black); }
  .thumb .mini-mark { position: absolute; left: 19px; top: 5px; width: 22px; height: 22px; border-radius: 50%; background: var(--brand); }
  .thumb .mini-brand { position: absolute; left: 4px; top: 30px; width: 52px; text-align: center; font-size: 5px; line-height: 6px; font-weight: 700; color: var(--brand); }
  .thumb .mini-contact { position: absolute; left: 14px; top: 45px; font-size: 4px; line-height: 5px; color: var(--contact); }
  .thumb .mini-centre { position: absolute; left: 0; right: 0; top: 26px; text-align: center; }
  .thumb .mini-centre .dot { width: 14px; height: 14px; border-radius: 50%; background: var(--white); margin: 0 auto 3px; }
  .thumb .mini-centre .word { font-size: 4px; font-weight: 700; color: var(--white); }

  .label { position: absolute; font-size: 36px; color: var(--label); line-height: 1; }
  .label--front { left: 186px; top: 803px; }
  .label--back { left: 772px; top: 803px; }
  .label--front-uv { left: 189px; top: 898px; }
  .label--back-uv { left: 776px; top: 898px; }

  .footer { position: absolute; left: 0; top: 974px; width: 1200px; height: 77px; background: var(--black); }
  .footer .notes { position: absolute; right: 23px; top: 8px; text-align: right; color: var(--white); font-style: italic; font-size: 24px; line-height: 30px; }
</style>
</head>
<body>
  <section class="card card--front" aria-label="Card front">
    <div class="feature-disc"></div>
    <div class="brand-block">
      <div class="brand-mark"></div>
      <div class="brand-name">KESTRELMOOR<br>HOLDINGS</div>
    </div>
    <div class="contact">
      <div class="name">Name Here</div>
      <div class="line position">Position</div>
      <div class="line">+63 900 555 0142</div>
      <div class="line">myemail@kestrelmoor.com</div>
      <div class="line">Manila, Philippines</div>
    </div>
  </section>

  <section class="card card--front-uv" aria-label="Card front UV layer">
    <div class="feature-disc"></div>
  </section>

  <section class="card card--back" aria-label="Card back">
    <div class="back-logo">
      <div class="brand-mark"></div>
      <div class="brand-name">KESTRELMOOR HOLDINGS</div>
    </div>
  </section>

  <section class="card card--back-uv" aria-label="Card back UV layer">
    <div class="back-logo">
      <div class="brand-mark"></div>
      <div class="brand-name">KESTRELMOOR HOLDINGS</div>
    </div>
  </section>

  <div class="thumb thumb--front">
    <div class="mini-disc"></div>
    <div class="mini-mark"></div>
    <div class="mini-brand">KESTRELMOOR<br>HOLDINGS</div>
    <div class="mini-contact">Name Here<br>Position<br>+63 900 555 0142<br>Manila</div>
  </div>
  <div class="label label--front">Front</div>

  <div class="thumb thumb--back">
    <div class="mini-centre"><div class="dot"></div><div class="word">KESTRELMOOR</div></div>
  </div>
  <div class="label label--back">Back</div>

  <div class="thumb thumb--front-uv">
    <div class="mini-disc"></div>
  </div>
  <div class="label label--front-uv">Front - UV Coated</div>

  <div class="thumb thumb--back-uv">
    <div class="mini-centre"><div class="dot"></div><div class="word">KESTRELMOOR</div></div>
  </div>
  <div class="label label--back-uv">Back - UV Coated</div>

  <footer class="footer">
    <div class="notes">* *Gray border - bleed area<br>* *Black area - UV Coated</div>
  </footer>
</body>
</html>
```